1 Page Bio, describing our Mission to buy multifamily properties in Colorado Springs.

I am uploading a sample of an associate who is doing a similar thing in Tampa Florida. I will also upload an attempt by my assistant to make the flyer and I will upload 3 pictures to use, along with another document that has text to add. I want to be able to edit the document pretty easily inside a google doc. thanks, I want it to look clean and professional.

```html
<!DOCTYPE html>
<html lang="en">
<head>
<meta charset="utf-8">
<title>Team Bio – Colorado Springs Multifamily</title>
<link href="https://fonts.googleapis.com/css2?family=Libre+Franklin:wght@400;500;600;700&display=swap" rel="stylesheet">
<style>
  :root {
    --teal: #68a39d;
    --teal-dark: #5a9c95;
    --teal-light: #9fcbc7;
    --slate: #5f6e77;
    --ink: #3a3f42;
    --name: #5a6166;
    --white: #ffffff;
    --backdrop: #e9e6e1;
  }
  * { box-sizing: border-box; margin: 0; padding: 0; }
  html, body { width: 1200px; height: 1200px; overflow: hidden; }
  body {
    background: var(--backdrop);
    font-family: "Libre Franklin", Arial, sans-serif;
    color: var(--ink);
    position: relative;
  }
  .sheet {
    position: absolute; left: 171px; top: 0;
    width: 857px; height: 1200px;
    background: var(--slate);
    overflow: hidden;
  }
  .top-band-accent {
    position: absolute; top: 0; left: 676px; width: 181px; height: 24px;
    background: var(--teal-light);
  }
  .side-panel {
    position: absolute; left: 0; top: 24px; width: 415px; height: 1176px;
    background: var(--teal);
    color: var(--white);
  }
  .team-photo {
    position: absolute; left: 27px; top: 2px; width: 369px; height: 248px;
    border: 4px solid var(--white);
    background: linear-gradient(160deg, #4f5b45 0%, #6b6a55 45%, #8a8272 100%);
    box-shadow: 0 2px 6px rgba(0,0,0,.25);
  }
  .side-block { position: absolute; left: 29px; width: 360px; }
  .side-title {
    font-weight: 700; font-size: 22px; line-height: 1;
    display: flex; align-items: center; gap: 16px; white-space: nowrap;
  }
  .side-title::after {
    content: ""; width: 48px; height: 2px; background: rgba(255,255,255,.75);
  }
  .side-title .light { font-weight: 500; }
  .side-text { font-size: 14px; line-height: 17px; margin-top: 14px; font-weight: 400; }
  .ticks { list-style: none; }
  .ticks li { position: relative; padding-left: 24px; }
  .ticks li::before {
    content: ""; position: absolute; left: 6px; top: 2px;
    width: 5px; height: 9px;
    border-right: 2px solid currentColor; border-bottom: 2px solid currentColor;
    transform: rotate(45deg);
  }
  .side-panel .ticks { margin-top: 16px; font-size: 14px; line-height: 17px; }
  .side-panel .ticks li { margin-bottom: 8px; }
  .contact-curve { position: absolute; left: 0; top: 0; }
  .portrait {
    position: absolute; top: 906px; width: 140px; height: 140px; border-radius: 50%;
    border: 3px solid var(--white);
    background: radial-gradient(circle at 50% 40%, #e6e6e6 0%, #bdbdbd 55%, #f2f2f2 100%);
  }
  .portrait.one { left: 40px; }
  .portrait.two { left: 211px; }
  .contact { position: absolute; left: 45px; top: 1052px; color: var(--white); }
  .contact-name { font-size: 20px; font-weight: 400; }
  .contact-phone {
    display: flex; align-items: center; gap: 8px;
    font-size: 37px; font-weight: 700; margin-top: 8px; letter-spacing: .5px;
  }
  .contact-mail { display: flex; align-items: center; gap: 10px; font-size: 20px; margin-top: 4px; }

  .team-panel {
    position: absolute; left: 415px; top: 24px; width: 442px; height: 1152px;
    background: var(--white);
  }
  .team-panel .block { position: absolute; left: 25px; width: 400px; }
  .team-title {
    position: absolute; left: 24px; top: 19px; height: 71px;
    border-left: 13px solid var(--slate);
    padding-left: 10px;
    font-size: 43px; font-weight: 600; color: var(--teal-dark);
    line-height: 71px;
  }
  .group-title {
    font-size: 23px; font-weight: 600; color: var(--teal-dark);
    display: flex; align-items: center; gap: 10px;
  }
  .group-title::after { content: ""; width: 48px; height: 2px; background: var(--teal-dark); }
  .person-name { font-size: 16.5px; font-weight: 500; color: var(--name); }
  .team-panel .ticks { margin-top: 16px; font-size: 14px; line-height: 16.5px; color: var(--teal-dark); }
  .team-panel .ticks li { margin-bottom: 8.5px; }
  .team-panel .ticks li span { color: var(--ink); }
  .team-panel .ticks.justify li span { display: block; text-align: justify; }
  .team-banner {
    font-size: 26px; font-weight: 700; color: var(--teal-dark); letter-spacing: .2px;
  }
</style>
</head>
<body>
<div class="sheet">
  <div class="top-band-accent"></div>

  <aside class="side-panel">
    <div class="team-photo" role="img" aria-label="Photo of the two principals standing together outdoors among trees"></div>

    <section class="side-block" style="top:289px">
      <h2 class="side-title">The Mission:</h2>
      <p class="side-text">To create a family business by purchasing<br>Multifamily Residences, one at a time.</p>
    </section>

    <section class="side-block" style="top:386px; left:27px;">
      <h2 class="side-title">Values:</h2>
      <p class="side-text" style="width:370px">To provide a white glove experience to all residences with a clean, safe, and fun environment</p>
    </section>

    <section class="side-block" style="top:490px">
      <h2 class="side-title">The Process:</h2>
      <p class="side-text">Buy right, manage right, and finance right.</p>
    </section>

    <section class="side-block" style="top:581px; width:380px">
      <h2 class="side-title">The Market: <span class="light">Colorado Springs</span></h2>
      <ul class="ticks">
        <li>Projected job growth of nearly 50%</li>
        <li>Below average unemployment rates.</li>
        <li>Above-average incomes.</li>
        <li>Solid economy, military, aerospace, electronics industry, and tourism</li>
      </ul>
    </section>

    <section class="side-block" style="top:768px">
      <h2 class="side-title">The Target:</h2>
      <p class="side-text">B and C class assets located in Colorado Springs or nearby submarkets.</p>
    </section>

    <svg class="contact-curve" width="415" height="1176" viewBox="0 0 415 1176" aria-hidden="true">
      <path d="M0 976 H335 Q415 976 415 1050 V1176 H0 Z" fill="var(--slate)"/>
    </svg>

    <div class="portrait one" role="img" aria-label="Black and white headshot of the first principal"></div>
    <div class="portrait two" role="img" aria-label="Black and white headshot of the second principal"></div>

    <div class="contact">
      <p class="contact-name">Rowan &amp; Curtis Ashby</p>
      <p class="contact-phone">
        <svg width="26" height="34" viewBox="0 0 26 34" aria-hidden="true">
          <path d="M7 2 L11 9 L8 12 Q9 19 14 24 L17 21 L23 26 L19 31 Q4 27 2 8 Z" fill="none" stroke="#fff" stroke-width="2.2" stroke-linejoin="round"/>
        </svg>
        555-201-4417
      </p>
      <p class="contact-mail">
        <svg width="30" height="18" viewBox="0 0 30 18" aria-hidden="true">
          <rect x="1" y="1" width="28" height="16" fill="none" stroke="#fff" stroke-width="1.8"/>
          <path d="M1 1 L15 11 L29 1 M1 17 L11 8 M29 17 L19 8" fill="none" stroke="#fff" stroke-width="1.8"/>
        </svg>
        rcashby@example.com
      </p>
    </div>
  </aside>

  <main class="team-panel">
    <h1 class="team-title">The Team</h1>

    <section class="block" style="top:123px">
      <h2 class="group-title">Principals</h2>
    </section>

    <section class="block" style="top:176px">
      <h3 class="person-name">Rowan Ashby</h3>
      <ul class="ticks">
        <li><span>Licensed Colorado Real Estate Agent 18 years.</span></li>
        <li><span>Broker-Owner of two HomeCrest Franchises 7 and 2 Years.</span></li>
        <li><span>Real Estate investing for 5 years.</span></li>
        <li><span>Member of Cornerstone Yield Academy.</span></li>
        <li><span>Married 24 years to Elaine, parenting 10 children together.</span></li>
        <li><span>Appeared on Dan and Leo's Unit by Unit podcast Episode 43</span></li>
        <li><span>$2M portfolio.</span></li>
      </ul>
    </section>

    <section class="block" style="top:453px">
      <h3 class="person-name">Curtis Ashby</h3>
      <ul class="ticks">
        <li><span>Retired Electrical Engineer.</span></li>
        <li><span>Active Real Estate Investor /Consultant.</span></li>
        <li><span>Net worth over $4M</span></li>
        <li><span>15 Grandchildren</span></li>
      </ul>
    </section>

    <section class="block" style="top:648px">
      <h2 class="team-banner">ROWAN &amp; CURTIS ASHBY</h2>
    </section>

    <section class="block" style="top:696px">
      <h2 class="group-title">Advisors</h2>
    </section>

    <section class="block" style="top:750px">
      <h3 class="person-name">Marcus Reed</h3>
      <ul class="ticks">
        <li><span>General partner on 103 Apartments</span></li>
        <li><span>Acquiring 101 more apartments in Q1 - 2020</span></li>
        <li><span>Flips 4-8 houses a year</span></li>
        <li><span>Active member in the Dan &amp; Leo Community</span></li>
        <li><span>Accountability coach</span></li>
      </ul>
    </section>

    <section class="block" style="top:928px">
      <h3 class="person-name">Walt Pruitt</h3>
      <ul class="ticks justify" style="margin-top:22px">
        <li><span>Walt is the owner/operator of Summit Residential Group and Summit Residential Management</span></li>
        <li><span>He has been in the real estate business for 13 years and has created a portfolio of over 1000 units while growing Summit Management with team of 15 staff members.</span></li>
        <li><span>He has taught real estate for the past 6 years and has dozens of highly successful students. Walt uses his extensive real estate experience to teach his students the “real” side of real estate.</span></li>
      </ul>
    </section>
  </main>
</div>
</body>
</html>
```